Tech website for innovative new Aerospace company

We need a website for our Aerospace tech business. We build Test equipment for major Aerospace companies like Veltrane. I would like to have a website that differentiates us from other companies like ours such as. The links below are whats typical in our line of work. You can see the "test systems" all over these sites. This is the type of thing we build. We have an innovative new way of building these test systems that will change how the entire industry views companies like mine. The website should be visually appealing and say to the customer they should expect more than just an information and link repository.

http://www.quorvix.com/
https://www.flinto-gear.de/en/
https://www.tessiro.com/en/home/

You can see there is just a bunch of stuff about the company whose site the customer has come to. Now the customer has to figure out how what they need might be organized in all of this noise about News and solutions, etc. I want a website that is very customer focused - meaning "what did they come here to do"? The closest I have seen to this is from another company like ours

https://www.marlokgroup.com/

Its still not quite what I'm looking for. Customers want to do more than just investigate potential areas of expertise I do want a part of the main page to say very clearly what it is we do, but the rest of it need to be customer focused around the task they want to do. Examples are

Learn about our modular system integration solution
Configure a test system
Get a quote or place an order
Get support
Browse products and get technical specs
Understand and lower your total cost of test
Company information
Contact us
Careers

Certain tasks like configure a system should be more prominent than others like company information

I'd like a few different types of pages designed

The product pages (don't need ecommerce) need to be hierarchical by category and allow engineers to find the product that meets their specs quickly. It should not be sales focused with too many moving marketing graphics. For example, those same pages displays the information

http://www.quorvix.com/products
https://www.flinto-gear.de/en/products/
https://www.tessiro.com/en/products/

The products, basic specs, price and links to manuals and data sheets should be prominently displayed and easy to compare between products

For marketing content I'd like a page design that allow for the content to be structured like a magazine page with infographics and visually appealing places to embed pictures and videos. I'll create content with info graphics that match the theme of the site. I'll need a content management system so that pages can be updated and modified to some extent without a professional website builder managing all content pushes.

For pages like support, ordering, getting a quote. It should be super easy for them to just get to where they need - whether they are looking for the phone number, contact form, downloadable order sheets etc

I am looking for a smart design concept with some dummy content in it. Once I winnow in on something that appeals to me I'll provide some more content to those I think are on the right track

Target Market(s)

Aerospace Engineers
Other Test equipment providers
Managers and leaders at Aerospace companies who are looking for a partner

Contact Information for Business Card

Need an upscale card

Coding

Coded - Design and coding required

Number of Pages Required

4 page

Font styles to use
Sans Serif

Colors
0555a3
f37122
474747
eaeaea

Requirements
Must have
• thicker cardstock
• two tone, different color on front and back
• bevel on one corner only
• Large size company logo with logo glossy or partially glossy. Surprise me with something visually and textually interesting
Nice to have
• I personally like the type of orange listed below, but it doesn't strictly fit into our blue/grey company colors. Would be glad to see someone make it work.
• Potentially orange on back side of cardstock, grey the other, or something like that
Should not have
• Dont look anything like a standard white business card, but don't go too crazy on layout. Still has to be crisp and professional for other high level executive recipients in the Aerospace industry

```html
<!DOCTYPE html>
<html lang="en">
<head>
<meta charset="utf-8">
<title>Aerovane — Modular Test System Solutions</title>
<link href="https://fonts.googleapis.com/css2?family=Montserrat:wght@400;600;700;800&family=Open+Sans:wght@400;600;700&display=swap" rel="stylesheet">
<style>
:root{
  --blue:#0555a3;
  --orange:#f37122;
  --grey:#474747;
  --light:#eaeaea;
  --navy:#0c1a3a;
  --navy-deep:#08132c;
  --white:#ffffff;
  --muted:#8a93a6;
}
*{box-sizing:border-box;margin:0;padding:0}
html,body{width:1200px;height:2652px;overflow:hidden}
body{position:relative;background:var(--white);font-family:"Open Sans",Arial,sans-serif;color:var(--grey);font-size:13px;line-height:1.6}
.abs{position:absolute}
.head-font{font-family:"Montserrat",Arial,sans-serif}

/* top strip */
.top-strip{left:420px;top:0;width:780px;height:40px;background:var(--navy);display:flex;align-items:center;padding-left:30px;color:var(--white);font-size:12px}
.top-strip .social{display:flex;gap:10px;margin-left:70px}
.top-strip .social span{width:20px;height:20px;border:1px solid rgba(255,255,255,.6);border-radius:50%}
.quote-btn{position:absolute;right:0;top:0;width:250px;height:40px;background:var(--orange);color:var(--white);font:700 13px "Montserrat",sans-serif;display:flex;align-items:center;justify-content:center;letter-spacing:.5px}

.logo{left:34px;top:22px;display:flex;align-items:center;gap:12px;font:800 40px/1 "Montserrat",sans-serif;color:var(--grey);letter-spacing:1px}
.logo i{width:18px;height:18px;background:var(--orange);display:block}

.contact-item{top:50px;display:flex;gap:10px;align-items:flex-start;font-size:11px;line-height:1.35}
.contact-item svg{flex:none;margin-top:2px}
.contact-item b{display:block;font:700 12px "Montserrat",sans-serif;color:var(--grey)}

/* hero */
.hero{left:380px;top:95px;width:820px;height:455px;background:linear-gradient(120deg,#5d6b7c 0%,#3a4a5e 45%,#6f7d8c 75%,#9aa4ae 100%)}
.hero-nav{left:380px;top:108px;width:820px;height:26px;background:rgba(12,26,58,.85);display:flex;gap:34px;padding-left:40px;align-items:center;font:600 11px "Montserrat",sans-serif;color:var(--white)}
.hero-nav span:first-child{background:var(--blue);padding:5px 12px;margin-left:-12px}
.hero-copy{left:520px;top:248px;color:var(--white)}
.hero-copy .kicker{font:600 22px "Montserrat",sans-serif}
.hero-copy h1{font:700 32px/1.2 "Montserrat",sans-serif;margin-top:2px}
.hero-copy p{font-size:12px;margin-top:12px;max-width:560px;line-height:1.5}
.hero-btns{display:flex;gap:12px;margin-top:34px}
.btn{height:36px;padding:0 20px;display:flex;align-items:center;font:700 11px "Montserrat",sans-serif;color:var(--white);letter-spacing:.4px}
.btn.orange{background:var(--orange)}
.btn.blue{background:var(--blue)}
.arrow{color:var(--white);font:400 34px/1 "Open Sans",sans-serif}

/* sidebar */
.side-nav{left:0;top:145px;width:380px;height:405px;background:var(--orange);display:flex;flex-direction:column}
.side-nav span{flex:1;display:flex;align-items:center;padding-left:28px;color:var(--white);font:700 19px "Montserrat",sans-serif;border-bottom:1px solid rgba(255,255,255,.45)}
.side-nav span:last-child{border-bottom:none}

/* about */
.eyebrow{font:700 12px "Montserrat",sans-serif;color:var(--orange);letter-spacing:.5px}
.about{left:40px;top:585px;width:590px}
.about h2{font:800 29px/1.2 "Montserrat",sans-serif;color:var(--grey);margin:4px 0 6px}
.about h2 em{font-style:normal;color:var(--orange)}
.rule{width:60px;height:3px;background:var(--orange);margin-bottom:16px}
.about p{font-size:12px;margin-bottom:12px}
.read-more{font:700 12px "Montserrat",sans-serif;color:var(--grey);margin-top:22px;display:inline-block;border-bottom:2px solid var(--orange)}
.about-photo{left:670px;top:600px;width:330px;height:280px;background:linear-gradient(160deg,#e9edf1,#c8d0d8 60%,#b7bfc8)}

/* band */
.band{left:0;top:935px;width:1200px;height:145px;background:linear-gradient(90deg,#1b2233 0%,#2c3545 55%,#3b4352 100%);padding:38px 40px;color:var(--white)}
.band small{font-size:11px;color:var(--orange);display:block}
.band h3{font:800 24px "Montserrat",sans-serif;margin-top:4px}
.band .btn{position:absolute;right:110px;top:50px;height:44px;padding:0 34px;font-size:13px}

/* products */
.products{left:0;top:1080px;width:1200px;height:360px;background:var(--light)}
.section-title{font:800 26px "Montserrat",sans-serif;color:var(--grey)}
.products .section-title{position:absolute;left:30px;top:28px}
.products .rule{position:absolute;left:30px;top:70px}
.pager{position:absolute;right:30px;top:36px;display:flex;gap:6px}
.pager span{width:22px;height:22px;background:var(--white);display:flex;align-items:center;justify-content:center;font-size:12px;color:var(--grey)}
.cards{position:absolute;left:30px;top:112px;display:flex;gap:20px}
.card{width:270px}
.card .img{height:126px;border:4px solid var(--white)}
.card h4{font:700 12px "Montserrat",sans-serif;color:var(--blue);margin:12px 0 4px}
.card p{font-size:11px;line-height:1.5}

/* expertise */
.expertise{left:0;top:1440px;width:1200px;text-align:center}
.expertise .section-title{margin-top:32px}
.expertise .section-title em{font-style:normal;color:var(--blue)}
.expertise .sub{font-size:11px;margin-top:6px}
.offer{top:1560px;width:390px;text-align:center}
.offer .img{height:230px}
.offer h4{font:600 18px "Montserrat",sans-serif;color:var(--grey);margin:30px 0 8px}
.offer p{font-size:11px;line-height:1.55}

/* footer */
.footer{left:0;top:2030px;width:1200px;height:622px;background:var(--navy);color:var(--white)}
.footer .f-logo{position:absolute;left:0;width:1200px;top:40px;display:flex;justify-content:center;align-items:center;gap:12px;font:800 38px/1 "Montserrat",sans-serif;color:var(--white);letter-spacing:1px}
.footer .f-logo i{width:16px;height:16px;background:var(--orange);display:block}
.footer .intro{position:absolute;left:330px;width:540px;top:112px;text-align:center;font-size:11px;color:#c9cfdb}
.f-col{top:2250px;font-size:11px;color:#c9cfdb}
.f-col h5{font:700 12px "Montserrat",sans-serif;color:var(--white);margin-bottom:14px}
.links{display:grid;grid-template-columns:100px 100px;row-gap:4px}
.f-social{display:flex;gap:10px}
.f-social span{width:26px;height:26px;border:1px solid rgba(255,255,255,.7);border-radius:50%}
.f-box{top:2420px;height:130px;background:var(--white);color:var(--grey);display:flex;align-items:center;gap:20px;padding:0 28px;font-size:12px;line-height:1.6}
.f-box svg{flex:none}
.copyright{left:0;top:2600px;width:1200px;border-top:1px solid rgba(255,255,255,.15);padding:14px 40px;font-size:10px;color:#9aa3b5}
</style>
</head>
<body>

<header>
  <div class="abs top-strip">
    <span>Welcome to our Aerovane</span>
    <div class="social"><span></span><span></span><span></span><span></span></div>
    <div class="quote-btn">GET A QUOTE</div>
  </div>
  <div class="abs logo"><i></i>AEROVANE</div>

  <div class="abs contact-item" style="left:432px">
    <svg width="16" height="22" viewBox="0 0 16 22"><path d="M8 0C3.6 0 0 3.5 0 7.8 0 13.6 8 22 8 22s8-8.4 8-14.2C16 3.5 12.4 0 8 0zm0 11a3 3 0 110-6 3 3 0 010 6z" fill="var(--orange)"/></svg>
    <div><b>Address</b>14 Larkmoor, CA 90410</div>
  </div>
  <div class="abs contact-item" style="left:760px">
    <svg width="22" height="16" viewBox="0 0 22 16"><rect width="22" height="16" rx="2" fill="var(--orange)"/><path d="M1 1l10 8 10-8" stroke="#fff" stroke-width="1.6" fill="none"/></svg>
    <div><b>Mail</b>solutions@aerovane-test.com</div>
  </div>
  <div class="abs contact-item" style="left:980px">
    <svg width="18" height="18" viewBox="0 0 18 18"><path d="M3.6 0l3 4-1.8 2.4a11 11 0 006.8 6.8L14 11.4l4 3-1.8 3.2C9 18.6-.6 9 .4 1.8z" fill="var(--orange)"/></svg>
    <div><b>Phone</b>+1 310 555 0142</div>
  </div>
</header>

<section>
  <div class="abs hero" role="img" aria-label="Engineer working at a modular aerospace test rack"></div>
  <nav class="abs hero-nav"><span>HOME</span><span>ABOUT US</span><span>PRODUCT</span><span>CAREERS</span><span>CONTACT US</span></nav>
  <div class="abs arrow" style="left:398px;top:300px">&#8249;</div>
  <div class="abs arrow" style="left:1170px;top:300px">&#8250;</div>
  <div class="abs hero-copy">
    <div class="kicker">Reinventing Test</div>
    <h1>With Modular System Solutions</h1>
    <p>Focus on what matters most – building a better product.<br>Our modular test systems shorten integration time and lower your total cost of test.</p>
    <div class="hero-btns"><span class="btn orange">VIEW SOLUTION</span><span class="btn blue">READ MORE</span></div>
  </div>
  <nav class="abs side-nav"><span>HOME</span><span>ABOUT US</span><span>PRODUCT</span><span>CAREERS</span><span>CONTACT US</span></nav>
</section>

<section class="abs about">
  <div class="eyebrow">ABOUT US</div>
  <h2>WELCOME TO <em>OUR AEROVANE</em></h2>
  <div class="rule"></div>
  <p>Aerovane has partnered with Corvane Instruments to develop a modular system architecture that allows for rapid design and integration of systems of any size. The key portion of a system that truly is universal between multiple products lives in the design layer, so configuration stays simple.</p>
  <p>Aerovane has partnered with Corvane Instruments to develop a modular system architecture that allows for rapid design and integration of systems of any size.</p>
  <span class="read-more">Read More</span>
</section>
<div class="abs about-photo" role="img" aria-label="Portrait of an Aerovane team member in business attire"></div>

<section class="abs band">
  <small>Aerovane is your partner in modular test</small>
  <h3>TEST STANDARD ON YOUR NEXT PRODUCT LINE</h3>
  <span class="btn orange">GET SUPPORT</span>
</section>

<section class="abs products">
  <h2 class="section-title">OUR PRODUCT</h2>
  <div class="rule"></div>
  <div class="pager"><span>&#8249;</span><span>&#8250;</span></div>
  <div class="cards">
    <article class="card">
      <div class="img" role="img" aria-label="Automated test rack photograph" style="background:linear-gradient(135deg,#8e98a4,#4e5a68)"></div>
      <h4>AUTOMATED TEST SOLUTIONS</h4>
      <p>Get to zero defects fast with our automated test solutions for inspection and machine vision needs.</p>
    </article>
    <article class="card">
      <div class="img" role="img" aria-label="Test system replication hardware photograph" style="background:linear-gradient(135deg,#b7c0c9,#6d7a88)"></div>
      <h4>TEST SYSTEM REPLICATION</h4>
      <p>Get to zero defects fast with our replicated test systems for inspection and machine vision needs.</p>
    </article>
    <article class="card">
      <div class="img" role="img" aria-label="Test products and platforms photograph" style="background:linear-gradient(135deg,#5a6470,#2c3440)"></div>
      <h4>TEST PRODUCTS &amp; PLATFORMS</h4>
      <p>Get to zero defects fast with our test platforms for inspection and machine vision needs.</p>
    </article>
    <article class="card">
      <div class="img" role="img" aria-label="Precision assembly equipment photograph" style="background:linear-gradient(135deg,#a6b0ba,#56616e)"></div>
      <h4>PRECISION ASSEMBLY</h4>
      <p>Get to zero defects fast with our precision assembly for inspection and machine vision needs.</p>
    </article>
  </div>
</section>

<section class="abs expertise">
  <h2 class="section-title">INDUSTRY <em>EXPERTISE</em></h2>
  <p class="sub">Proven ideas in automated Prototyping, Verification &amp; Validation, Production and Aftermarket Testing for<br>Aerospace OEM Programs</p>
</section>
<article class="abs offer" style="left:130px">
  <div class="img" role="img" aria-label="Engineers assembling a modular test system" style="background:linear-gradient(135deg,#7b8794,#3e4a58)"></div>
  <h4>Modular System Solutions</h4>
  <p>Our innovative new system-level platform can dramatically improve your test schedule while controlling project risk and equipment budget.</p>
</article>
<article class="abs offer" style="left:680px">
  <div class="img" role="img" aria-label="Test equipment control panel close-up" style="background:linear-gradient(135deg,#4f6f8f,#1f3550)"></div>
  <h4>Aerovane Offerings</h4>
  <p>From hardware and software configuration services to complete standardization solutions, we can help you achieve your test program.</p>
</article>

<footer>
  <div class="abs footer">
    <div class="f-logo"><i></i>AEROVANE</div>
    <p class="intro">Aerovane has partnered with Corvane Instruments to develop a modular system architecture that allows for rapid design.</p>
  </div>
  <div class="abs f-col" style="left:130px;width:260px">
    <h5>ABOUT US</h5>
    <p>From the founders to the engineers, to the students, there is a path. From the founders to the students, to the industry there is a path.</p>
  </div>
  <div class="abs f-col" style="left:520px">
    <h5>QUICK LINK</h5>
    <div class="links"><span>Home</span><span>Careers</span><span>About Us</span><span>Contact</span><span>Product</span></div>
  </div>
  <div class="abs f-col" style="left:880px">
    <h5>SOCIAL LINK</h5>
    <div class="f-social"><span></span><span></span><span></span><span></span></div>
  </div>

  <div class="abs f-box" style="left:132px;width:336px">
    <svg width="26" height="36" viewBox="0 0 16 22"><path d="M8 0C3.6 0 0 3.5 0 7.8 0 13.6 8 22 8 22s8-8.4 8-14.2C16 3.5 12.4 0 8 0zm0 11a3 3 0 110-6 3 3 0 010 6z" fill="var(--blue)"/></svg>
    <span>14 Larkmoor, CA 90410</span>
  </div>
  <div class="abs f-box" style="left:482px;width:318px">
    <svg width="30" height="30" viewBox="0 0 18 18"><path d="M3.6 0l3 4-1.8 2.4a11 11 0 006.8 6.8L14 11.4l4 3-1.8 3.2C9 18.6-.6 9 .4 1.8z" fill="var(--blue)"/></svg>
    <span>Official Fax: 310 555 0187<br>Official Phone: 310 555 0193</span>
  </div>
  <div class="abs f-box" style="left:814px;width:338px">
    <svg width="34" height="24" viewBox="0 0 22 16"><rect width="22" height="16" rx="2" fill="var(--blue)"/><path d="M1 1l10 8 10-8" stroke="#fff" stroke-width="1.6" fill="none"/></svg>
    <span>Email: solutions@aerovane-test.com<br>www.aerovane-test.com</span>
  </div>
  <div class="abs copyright">© 2018 All Rights Reserved.</div>
</footer>

</body>
</html>
```